International Luxury Furniture and Accessories Outsourcing Company

We Need a Business Card design for a new Outsourcing company doing Business Internationally in the Luxury Furniture and Accessories Space. The company's name is MARCUS BELLWOOD and we deal with clients in the high end and Luxury Space for Furniture and Accessories in the world. We would like Designs that speaks Luxury and Professionalism.

We like the Combination of the color Brown and Gold or Black and Gold. We are also open to other color combo.

We like some of the design of file attached.
Updates

This is Peter and We really appreciate all of you taking the time out and putting the effort to help us jump start our new company. We have 2-3 designs that we like and will decide soon to pick one. Once again, Thank you to all of you !! Best Regards, Peter

Industry/Entity Type

Business

```html
<!DOCTYPE html>
<html lang="en">
<head>
<meta charset="utf-8">
<title>Marcus Bellwood – Business Card</title>
<link rel="stylesheet" href="https://fonts.googleapis.com/css2?family=Exo+2:wght@600&family=Open+Sans:wght@400;600&display=swap">
<style>
  :root {
    --backdrop: #e9e4dd;
    --card-top: #b8402f;
    --card-bottom: #86160f;
    --gold: #f4c400;
    --ink-light: #fbeee0;
  }
  * { box-sizing: border-box; margin: 0; padding: 0; }
  html, body { width: 1200px; height: 900px; overflow: hidden; }
  body { background: var(--backdrop); position: relative; font-family: "Open Sans", sans-serif; }

  .card {
    position: absolute;
    width: 560px; height: 320px;
    background: linear-gradient(160deg, var(--card-top), var(--card-bottom));
    border-radius: 4px;
    box-shadow: 0 10px 24px rgba(60, 20, 10, .25);
  }
  .card__frame {
    position: absolute; inset: 16px;
    border: 3px solid var(--gold);
  }
  .card--front { left: 80px; top: 110px; }
  .card--back { left: 560px; top: 470px; }

  .brand {
    display: flex; align-items: center; gap: 14px;
    font-family: "Exo 2", sans-serif; font-weight: 600;
    color: var(--gold);
  }
  .brand__square { width: 22px; height: 22px; background: var(--gold); flex: none; }

  .front__content {
    position: absolute; inset: 0;
    display: flex; flex-direction: column; align-items: center; justify-content: center; gap: 34px;
  }
  .front__content .brand { font-size: 40px; letter-spacing: 1px; }
  .front__web { color: var(--gold); font-size: 15px; letter-spacing: .5px; }

  .back__mark {
    position: absolute; left: 44px; top: 0; bottom: 0; width: 230px;
    display: flex; align-items: center;
  }
  .back__mark .brand { font-size: 22px; gap: 10px; line-height: 1.1; }
  .back__mark .brand__square { width: 16px; height: 16px; }
  .back__divider {
    position: absolute; left: 300px; top: 54px; width: 2px; height: 212px;
    background: var(--gold);
  }
  .back__details {
    position: absolute; left: 326px; top: 66px; right: 30px;
    color: var(--ink-light); font-size: 13px;
  }
  .back__name { color: var(--gold); font-size: 15px; letter-spacing: .5px; }
  .back__role { font-size: 13px; margin-bottom: 16px; }
  .contact { list-style: none; display: flex; flex-direction: column; gap: 7px; }
  .contact li { display: flex; align-items: flex-start; gap: 8px; line-height: 1.3; }
  .contact svg { width: 11px; height: 11px; flex: none; margin-top: 3px; fill: var(--gold); }
  .contact__address { margin-top: 8px; }
</style>
</head>
<body>

<section class="card card--front" aria-label="Card front">
  <div class="card__frame"></div>
  <div class="front__content">
    <div class="brand"><span class="brand__square"></span>Marcus Bellwood</div>
    <p class="front__web">www.bellwoodtrade.com</p>
  </div>
</section>

<section class="card card--back" aria-label="Card back">
  <div class="card__frame"></div>
  <div class="back__mark">
    <div class="brand"><span class="brand__square"></span>Marcus<br>Bellwood</div>
  </div>
  <div class="back__divider"></div>
  <div class="back__details">
    <p class="back__name">PETER LAWSON</p>
    <p class="back__role">Designation</p>
    <ul class="contact">
      <li>
        <svg viewBox="0 0 24 24" aria-hidden="true"><path d="M6.6 10.8a15 15 0 0 0 6.6 6.6l2.2-2.2a1 1 0 0 1 1-.25 11.4 11.4 0 0 0 3.6.57 1 1 0 0 1 1 1V20a1 1 0 0 1-1 1A17 17 0 0 1 3 4a1 1 0 0 1 1-1h3.5a1 1 0 0 1 1 1c0 1.25.2 2.45.57 3.57a1 1 0 0 1-.25 1z"/></svg>
        +100 555 0182
      </li>
      <li>
        <svg viewBox="0 0 24 24" aria-hidden="true"><path d="M2 5h20v14H2z M3 6l9 7 9-7" stroke="#86160f" stroke-width="1.5"/></svg>
        peter@bellwoodtrade.com
      </li>
      <li class="contact__address">
        <svg viewBox="0 0 24 24" aria-hidden="true"><path d="M12 3 2 12h3v9h5v-6h4v6h5v-9h3z"/></svg>
        <span>Building No, Street No,<br>City, Zip Code</span>
      </li>
    </ul>
  </div>
</section>

</body>
</html>
```